Coffeeshop menu for filter tip

We want to have a cannabis (coffeeshop) menu in the size 25mm wide x 60mm wide. Some examples attached.

it must have the following text:
Menu

WEED p/g
Velotrine €16
Cinderfox €14
Tide Rambler €14
Marigolden €16
Grand Pelican €14
Copper Comet €14

HASH p/g
Baltic Ember €12
Harbor Velvet€11
Plum Rova €14
Dusk Maple €10

Target Market(s)

tourist in Amsterdam

Requirements
Nice to have
• cannabis sign leaf
• No Cigarettes allowed symbol

```html
<!DOCTYPE html>
<html lang="en">
<head>
<meta charset="utf-8">
<title>Coffeeshop Menu</title>
<link rel="stylesheet" href="https://fonts.googleapis.com/css2?family=Londrina+Solid:wght@400;900&family=Gochi+Hand&display=swap">
<style>
  :root {
    --header-bg: #2c302b;
    --body-bg: #3a3834;
    --text: #ffffff;
    --leaf-green: #2f4a2a;
    --leaf-edge: rgba(47, 74, 42, 0);
  }
  * { margin: 0; padding: 0; box-sizing: border-box; }
  html, body {
    width: 1200px;
    height: 2884px;
    overflow: hidden;
    background: var(--body-bg);
  }
  .menu {
    position: relative;
    width: 1200px;
    height: 2884px;
    background: var(--body-bg);
    color: var(--text);
    font-family: "Gochi Hand", cursive;
  }
  .menu-header {
    position: absolute;
    left: 0; top: 0;
    width: 1200px;
    height: 358px;
    background: var(--header-bg);
  }
  .menu-title {
    position: absolute;
    left: 66px;
    top: 40px;
    font-family: "Londrina Solid", sans-serif;
    font-weight: 900;
    font-size: 290px;
    line-height: 1;
    letter-spacing: 6px;
  }
  .leaf-art {
    position: absolute;
    left: 163px;
    top: 1017px;
    width: 955px;
    height: 1058px;
    background: radial-gradient(ellipse at 55% 50%, var(--leaf-green) 0%, rgba(47,74,42,0.7) 35%, var(--leaf-edge) 70%);
  }
  .section {
    position: absolute;
    left: 73px;
  }
  .section-weed { top: 560px; }
  .section-hash { top: 1870px; }
  .section-heading {
    font-size: 190px;
    line-height: 200px;
    font-weight: 400;
    letter-spacing: 2px;
  }
  .section-unit { font-size: 104px; }
  .price-list { list-style: none; }
  .price-item {
    font-size: 112px;
    line-height: 98px;
    letter-spacing: 1px;
    white-space: nowrap;
  }
</style>
</head>
<body>
<main class="menu">
  <header class="menu-header">
    <h1 class="menu-title">MENU</h1>
  </header>

  <div class="leaf-art" role="img" aria-label="Large cannabis leaf illustration behind the price list"></div>

  <section class="section section-weed">
    <h2 class="section-heading">Weed <span class="section-unit">(p/g)</span></h2>
    <ul class="price-list">
      <li class="price-item">Velotrine €16</li>
      <li class="price-item">Cinderfox €14</li>
      <li class="price-item">Tide Rambler €14</li>
      <li class="price-item">Marigolden €16</li>
      <li class="price-item">Grand Pelican €14</li>
      <li class="price-item">Copper Comet €14</li>
    </ul>
  </section>

  <section class="section section-hash">
    <h2 class="section-heading">Hash <span class="section-unit">(p/g)</span></h2>
    <ul class="price-list">
      <li class="price-item">Baltic Ember €12</li>
      <li class="price-item">Harbor Velvet €11</li>
      <li class="price-item">Plum Rova €14</li>
      <li class="price-item">Dusk Maple €10</li>
    </ul>
  </section>
</main>
</body>
</html>
```